QLM WEBSITE
QLM PRODUCTIONS
• 31 octobre 2011 11:36 wtz48307
i really like the menu bar treatment that i previously uploaded with the orange swipe under.
• 31 octobre 2011 11:34 wtz48307
hello all, i am torn between several designs because there are many elements of each that i love. i am going to upload clips of certain elements of each that i like for you to try and see if you can incorporate. i will also specifically send you notes for each of your designs. i'd like to get this wrapped up asap! thank you for all your great work!
• 26 octobre 2011 16:13 wtz48307
here it is...
Link to file:
https://files.parcelvane.example/Xq7rLm2VbN9kTs4Hw
please note that i would still like to see something about products/services that we have done. and also try to incorporate the current tagline from the logo, or the one on the attached, or "The Most Trusted Name in QLM TV"
thanks!
• 26 octobre 2011 16:07 wtz48307
i will be uploading a design sample. i'd like to see your version of this using my new logo design and colors. thanks!
• 26 octobre 2011 08:01 BrightQuillStudio
thanks,
BrightQuillStudio
• 26 octobre 2011 00:01 velumorrin
• 24 octobre 2011 16:09 wtz48307
hello all. ok, getting some good ideas, but nothing is standing out as a workable concept. there are great things about each which i have sent to you in private emails.
a few general thoughts on content for the main page.
id like to use the pinks and orange of the logo to highlight certain creative elements elements...i'd also like to have all headlines not in a block of color, but as a stand alone. these headlines will change, so please also utilize a creative font. in lieu of having 5 or so separate videos to highlight out work, let's try using just one demo video clip instead. but i do want an area on the page that highlights some products/logos with images, so that in a snapshot the visitor can quickly see the scope of our work on the main page. and again maybe we just highlight one or two testimonials. thanks!
• 23 octobre 2011 20:20 wtz48307
another comment is that this is a complete re-design of the site...so i don't want any old graphic elements of the current site, such as the arrow pointing to the testimonials. everything should be designed around the new logo, color and those design elements only.
thanks.
• 23 octobre 2011 19:26 wtz48307
please look at this website as well.
http://www.plotandframe.example/
• 22 octobre 2011 14:35 wtz48307
also, there should not be any other images on the site other than something that is related to our clients.
• 22 octobre 2011 11:37 wtz48307
please make sure to read the above comments. we are a creative services company. not a product company. think of an advertising agency website....creative, unusual, unique, clean, not busy.
• 22 octobre 2011 11:14 ToRuVex7Gk4Lab
Hi JL,
please feel free to let me know the required changes so that your expectations are met.
Awaiting for your kind feedback
ToruVex
• 22 octobre 2011 10:37 wtz48307
make sure to look at www.quellbornstudio.example i like that site.
• 22 octobre 2011 10:34 wtz48307
also, feel free to greek out any text/headline....we are planning on changing the copy anyway, so you can create a design that we would write to.
• 22 octobre 2011 10:31 wtz48307
#3 is tooooo busy...too many elements on the page....need to keep it clean, yet powerful. really emphasize our variety and creativity in our work with a powerful testimonial(s).
• 19 octobre 2011 13:15 wtz48307
just made the project veiled.
• 19 octobre 2011 11:49 wtz48307
this is a good first start, but the images are not appropriate. we need to either show product pictures, company logos, etc of some of the productions we've shot. we cannot have images that are unrelated to what we do. look at the bold, clean design of www.quellbornstudio.example i like how the testimonials are very prominent. the main page needs to have a prominent testimonial or a way to show many testimonials as well as highlighting a few of our top campaigns, but keeping it very clean and simple. i can create one video to highlight these shows, but the main page needs to have a quick snapshot of the scope of work that we have done. i would use Bramlux/tintslates as one to highlight, little minds leap, stormy plains, and one of our newest commercials harborstone credit...i'll upload that commercial. if you want me to upload the quicktimes or artwork of any of these commercials, please let me know. one thing i do like about #2 is the diagonal design with the colors behind it. also, i'd like to have the nav buttons on the right side, going down the right side of the page...just something more creative and interesting.
• 17 octobre 2011 21:07 wtz48307
PLEASE MAKE SURE TO SEE THE UPLOADED NEW ARTWORK FOR MY NEW LOGO. THANKS!
• 17 octobre 2011 16:30 wtz48307
some more comments to add to the creative brief...this may be more that just the home page, but i'm putting all my thoughts together for you.
1. i'd like to showcase certain commercials by providing the project name and details
2. maybe some transitions with camera shutter sound effects
3. need a "guestbook"...probably not for main page.
4. should include all social media icons

```html
<!DOCTYPE html>
<html lang="en">
<head>
<meta charset="utf-8">
<title>QLM Productions</title>
<link href="https://fonts.googleapis.com/css2?family=Open+Sans:ital,wght@0,400;0,600;0,700;1,400;1,700&display=swap" rel="stylesheet">
<style>
  :root {
    --orange: #f39322;
    --magenta: #e0197d;
    --plum: #9c1f63;
    --plum-dark: #7f184f;
    --ink: #222222;
    --grey: #555555;
    --white: #ffffff;
    --soft-pink: #f6d3e4;
  }
  * { box-sizing: border-box; margin: 0; padding: 0; }
  html, body { width: 1200px; height: 889px; overflow: hidden; background: var(--white); }
  body { font-family: "Open Sans", Arial, sans-serif; color: var(--ink); position: relative; }

  .site {
    position: absolute; left: 101px; top: 19px; width: 998px; height: 805px;
    border: 4px solid var(--orange); background: var(--white);
  }

  .signup { position: absolute; left: 34px; top: 12px; }
  .signup h2 { font-size: 13px; font-weight: 700; color: var(--magenta); margin-bottom: 8px; }
  .signup input {
    display: block; width: 178px; height: 20px; margin-bottom: 9px;
    border: 1px solid var(--orange); background: #fff6ef;
    font-family: inherit; font-size: 10px; color: var(--orange); padding: 0 6px;
  }
  .signup input::placeholder { color: var(--orange); opacity: .8; }

  .services { position: absolute; left: 163px; top: 160px; font-size: 10.5px; color: var(--ink); }
  .services a { color: var(--magenta); text-decoration: none; }

  .showcase-main {
    position: absolute; left: 170px; top: 189px; width: 360px; height: 330px;
    border: 7px solid var(--magenta); background: var(--white);
  }
  .showcase-art {
    position: absolute; left: 60px; top: 18px; width: 206px; height: 232px;
    background: linear-gradient(160deg, #f2c23a 0%, #6fb3e0 45%, #3a8fd0 100%);
    border-radius: 4px;
  }
  .player {
    position: absolute; left: 0; right: 0; bottom: 0; height: 56px;
    background: linear-gradient(#c2377b, #8e1a55); padding: 8px 12px;
  }
  .player-title { font-size: 14px; color: #ffd9ea; }
  .player-controls { position: absolute; left: 12px; bottom: 9px; display: flex; align-items: center; gap: 6px; }
  .player-track { width: 270px; height: 4px; background: #f4c6dc; border-radius: 2px; position: relative; }
  .player-track span { position: absolute; left: 0; top: 0; height: 4px; width: 110px; background: var(--white); border-radius: 2px; }

  .thumbs { position: absolute; left: 540px; top: 189px; width: 81px; height: 330px; border: 5px solid var(--magenta); display: flex; flex-direction: column; gap: 5px; background: var(--magenta); }
  .thumb { flex: 1; background: var(--white); position: relative; }
  .thumb i { position: absolute; inset: 10px 16px; border-radius: 3px; }

  .testimonial { position: absolute; left: 0; width: 778px; top: 585px; text-align: center; }
  .testimonial blockquote { font-size: 17px; line-height: 27px; color: var(--grey); }
  .testimonial blockquote strong { color: var(--ink); font-weight: 700; }
  .testimonial .mark { font-size: 34px; font-weight: 700; color: var(--ink); line-height: 0; position: relative; top: 8px; }
  .testimonial cite { display: block; margin-top: 18px; font-size: 17px; font-style: normal; color: var(--ink); }
  .testimonial cite b { font-weight: 700; }
  .testimonial cite em { font-style: italic; }

  .social { position: absolute; left: 34px; bottom: 10px; display: flex; align-items: center; gap: 14px; font-size: 10px; font-weight: 700; }
  .social a { color: var(--magenta); text-decoration: none; }
  .social span { width: 1px; height: 12px; background: var(--orange); }

  .sidebar { position: absolute; right: 0; top: 0; width: 218px; height: 100%; background: var(--plum); }
  .utility { list-style: none; position: absolute; left: 54px; top: 20px; font-size: 11px; line-height: 17px; }
  .utility a { color: var(--white); text-decoration: none; }
  .brand {
    position: absolute; left: 5px; top: 116px; width: 209px; height: 145px;
    display: flex; flex-direction: column; align-items: center; justify-content: center; gap: 12px;
  }
  .brand-row { display: flex; align-items: center; gap: 8px; }
  .brand-square { width: 14px; height: 14px; background: var(--orange); }
  .brand-name { font-size: 17px; font-weight: 700; color: var(--white); letter-spacing: .3px; white-space: nowrap; }
  .brand-tag { font-size: 11px; color: var(--soft-pink); }
  .menu { list-style: none; position: absolute; left: 0; top: 281px; width: 100%; }
  .menu li { height: 47px; border-bottom: 1px solid var(--plum-dark); }
  .menu a { display: block; line-height: 46px; padding-left: 62px; color: var(--white); font-size: 13px; font-weight: 700; text-decoration: none; }
  .menu .active { background: var(--orange); }
</style>
</head>
<body>
  <div class="site">
    <section class="signup">
      <h2>Sign up</h2>
      <input type="text" placeholder="Type email">
      <input type="password" placeholder="Password">
    </section>

    <p class="services">Health services, <a href="#">Financial services</a>, <a href="#">Insurance services</a>, <a href="#">Banking services</a>, <a href="#">Health services</a>,</p>

    <section class="showcase-main">
      <div class="showcase-art" role="img" aria-label="Product box of the little minds leap campaign"></div>
      <div class="player">
        <div class="player-title">1/4. Little minds leap</div>
        <div class="player-controls">
          <svg width="40" height="12" viewBox="0 0 40 12">
            <path d="M2 2v8M4 6l6-4v8z" fill="#fff" stroke="#fff" stroke-width="1.5"/>
            <circle cx="20" cy="6" r="5" fill="#fff"/>
            <path d="M18.5 3.5v5l4-2.5z" fill="#9c1f63"/>
            <path d="M30 2l6 4-6 4zM38 2v8" fill="#fff" stroke="#fff" stroke-width="1.5"/>
          </svg>
          <div class="player-track"><span></span></div>
        </div>
      </div>
    </section>

    <section class="thumbs" aria-label="Campaign thumbnails">
      <div class="thumb"><i role="img" aria-label="Campaign product box" style="background:linear-gradient(#f2c23a,#3a8fd0)"></i></div>
      <div class="thumb"><i role="img" aria-label="Campaign product bottle" style="background:linear-gradient(#d9e6ef,#6fa4c9)"></i></div>
      <div class="thumb"><i role="img" aria-label="Campaign pump bottle" style="background:linear-gradient(#e7b0b8,#d23c3c)"></i></div>
      <div class="thumb"><i role="img" aria-label="Campaign product box" style="background:linear-gradient(#f2c23a,#3a8fd0)"></i></div>
    </section>

    <section class="testimonial">
      <blockquote>
        <span class="mark">“</span>With have a <strong>terrific relationship</strong> with Dana and her company.<br>
        We look forward to many <strong>more successful</strong> campaigns in the future<span class="mark">”</span>
      </blockquote>
      <cite>-<b>Marco Fenwick,</b> <em>Fenwick Beauty</em></cite>
    </section>

    <nav class="social">
      <a href="#">Circlepost</a><span></span>
      <a href="#">Chirpline</a><span></span>
      <a href="#">Workmesh</a><span></span>
      <a href="#">Clipstream</a>
    </nav>

    <aside class="sidebar">
      <ul class="utility">
        <li><a href="#">blog</a></li>
        <li><a href="#">newsletter</a></li>
        <li><a href="#">press release</a></li>
        <li><a href="#">how we give back</a></li>
      </ul>
      <div class="brand">
        <div class="brand-row"><span class="brand-square"></span><span class="brand-name">QLM PRODUCTIONS</span></div>
        <div class="brand-tag">The Most Trusted Name in QLM TV</div>
      </div>
      <ul class="menu">
        <li class="active"><a href="#">home</a></li>
        <li><a href="#">what we do</a></li>
        <li><a href="#">portfolio</a></li>
        <li><a href="#">client list</a></li>
        <li><a href="#">body of work</a></li>
        <li><a href="#">contact us</a></li>
      </ul>
    </aside>
  </div>
</body>
</html>
```